Real Estate agent needs flyer/folder to contain bio and overview of services

I'm including files of the layout of the small folder. The folder is 6 1/2 across and 9 1/2 inches long. It will have a front & back cover and then writing on the 2 inside pages.

I am sending a few files to incorporate into the flyer, 1 new logo to use and 2 files which are coloring ideas.

```html
<!DOCTYPE html>
<html lang="en">
<head>
<meta charset="utf-8">
<title>Marisa Castellan Realtor Folder</title>
<link rel="stylesheet" href="https://fonts.googleapis.com/css2?family=Mulish:wght@600;700;800&family=Arimo:ital,wght@0,400;0,700;1,700&display=swap">
<style>
  :root {
    --teal-light: #76efe2;
    --teal-mid: #45c8c6;
    --teal-deep: #29aeb4;
    --accent-red: #d2473f;
    --body-gray: #4a535c;
    --ink: #2b2f33;
    --brand-blue: #1458d6;
    --sky-pale: #e6eef7;
    --sand-pale: #f3ede4;
    --paper: #ffffff;
  }
  * { margin: 0; padding: 0; box-sizing: border-box; }
  html, body { width: 1200px; height: 876px; overflow: hidden; background: var(--paper); }
  .folder { position: relative; width: 1200px; height: 876px; }

  .back-cover {
    position: absolute; left: 0; top: 0; width: 599px; height: 876px;
    background: radial-gradient(ellipse 420px 520px at 215px 450px, var(--teal-light) 0%, var(--teal-mid) 55%, var(--teal-deep) 100%);
  }
  .headline {
    position: absolute; left: 0; top: 262px; width: 610px; text-align: center;
    font-family: "Arimo", Arial, sans-serif; font-style: italic; font-weight: 700;
    font-size: 25px; line-height: 29px; color: var(--accent-red);
  }
  .bio {
    position: absolute; left: 19px; top: 592px; width: 580px;
    font-family: "Mulish", sans-serif; font-weight: 700;
    font-size: 20.5px; line-height: 26.5px; color: var(--body-gray);
  }
  .contact {
    position: absolute; left: 0; top: 749px; width: 586px; text-align: center;
    font-family: "Arimo", Arial, sans-serif; font-size: 18.5px; line-height: 23px; color: var(--ink);
  }
  .contact-name { font-weight: 700; font-size: 22px; line-height: 26px; color: var(--accent-red); }

  .front-cover { position: absolute; left: 600px; top: 0; width: 600px; height: 876px; }
  .front-cover svg { display: block; }

  .agent-mark {
    position: absolute; left: 669px; top: 300px; width: 424px; text-align: center;
    font-family: "Mulish", sans-serif; font-weight: 800; color: var(--brand-blue);
    font-size: 44px; line-height: 50px; letter-spacing: 1px;
  }
  .agent-title {
    position: absolute; left: 669px; top: 495px; width: 424px; text-align: center;
    font-family: "Mulish", sans-serif; font-weight: 700; color: var(--ink);
    font-size: 17px; letter-spacing: 1px;
  }
  .brokerage {
    position: absolute; left: 612px; top: 760px; width: 160px; text-align: center;
    font-family: "Mulish", sans-serif; font-weight: 800; font-size: 19px; color: var(--accent-red);
  }
</style>
</head>
<body>
<main class="folder">
  <section class="back-cover">
    <p class="headline">Discover New Comfort In Real Estate.<br>Choose Marisa Castellan Realtors</p>
    <p class="bio">Along with being your Realtor, I’m a lifelong resource for all things home-related &amp; beyond… If you need a great referral for anything at all, call me! I can’t wait to work with you!</p>
    <address class="contact" style="font-style: normal;">
      <div class="contact-name">Marisa Castellan</div>
      <div>555 014 2387</div>
      <div>Marisa@castellanhomes.com</div>
      <div>www.castellanhomes.com</div>
    </address>
  </section>

  <section class="front-cover">
    <svg width="600" height="876" viewBox="600 0 600 876">
      <defs>
        <clipPath id="cover-curve">
          <path d="M600 0 H1085 C1160 40 1196 250 1198 440 C1196 640 1150 830 1060 876 H600 Z"/>
        </clipPath>
        <linearGradient id="pale-photo" x1="0" y1="0" x2="0" y2="1">
          <stop offset="0" stop-color="var(--sky-pale)"/>
          <stop offset="0.5" stop-color="#eceff2"/>
          <stop offset="1" stop-color="var(--sand-pale)"/>
        </linearGradient>
        <linearGradient id="teal-photo" x1="0" y1="0" x2="1" y2="1">
          <stop offset="0" stop-color="#4dbfcb"/>
          <stop offset="0.5" stop-color="#5ccac8"/>
          <stop offset="1" stop-color="#3fa9a8"/>
        </linearGradient>
      </defs>
      <g clip-path="url(#cover-curve)" role="img" aria-label="Faded photograph of a house entrance with palm trees under a teal tint">
        <rect x="600" y="0" width="272" height="876" fill="url(#pale-photo)"/>
        <rect x="872" y="0" width="330" height="876" fill="url(#teal-photo)"/>
      </g>
      <line x1="600" y1="0" x2="600" y2="876" stroke="var(--paper)" stroke-width="2"/>
      <circle cx="881" cy="391" r="212" fill="var(--paper)"/>
    </svg>
  </section>

  <div class="agent-mark">MARISA<br>CASTELLAN</div>
  <div class="agent-title">REALTOR®</div>
  <div class="brokerage">Summit Realty</div>
</main>
</body>
</html>
```